Brennwald Metrics GmbH
Brennwald Metrics GmbH - Financial Services
Creative Brief
Professional
Lionel T Brennwald
Managing Director
Lindenweg 42 CH-6300 Zug Switzerland
U.S. Telephone 203.555.0186
lionel.brennwald@brennwaldmetrics-example.ch
brennwaldmetrics-example.ch
Wedsite will have partial moon crater stripped across the top. It might be interesting on the business card. Hard to tell if it will be too busy. JPG attached. Else simple is better. Note that address is broken after 19, and after Zug. It doesn't show on the confirmation. Kindly upload business cards and stationary, not just Business cards. It has to be a package

```html
<!DOCTYPE html>
<html lang="en">
<head>
<meta charset="utf-8">
<title>Brennwald Metrics GmbH – Stationery Package</title>
<link rel="stylesheet" href="https://fonts.googleapis.com/css2?family=Cinzel:wght@400;700&display=swap">
<style>
  :root{
    --backdrop:#e6e6e4;
    --paper:#ffffff;
    --navy:#163a78;
    --blue:#1f6fc4;
    --sky:#4fa3e6;
    --pale:#dbeaf6;
    --ink:#3a4a5e;
    --grey:#8a96a3;
  }
  *{margin:0;padding:0;box-sizing:border-box}
  html,body{width:1200px;height:901px;overflow:hidden;background:var(--backdrop)}
  body{position:relative;font-family:"Cinzel",serif;color:var(--ink)}
  .sheet{position:absolute;background:var(--paper);box-shadow:0 2px 6px rgba(0,0,0,.18);overflow:hidden}
  .brand{position:absolute;display:flex;align-items:center;gap:8px}
  .brand__square{background:var(--navy);flex:none}
  .brand__name{font-family:"Cinzel",serif;font-weight:700;color:var(--navy);text-transform:uppercase;line-height:1.05;letter-spacing:.5px;white-space:nowrap}
  .edge-band{position:absolute;left:0;top:0;bottom:0;background:linear-gradient(180deg,var(--sky) 0%,var(--blue) 45%,var(--navy) 75%,rgba(22,58,120,0) 100%)}
  .ghost-square{position:absolute;background:var(--pale);opacity:.75;border-radius:6px}
  .site{position:absolute;font-size:10px;letter-spacing:1px;color:var(--ink);font-variant:small-caps;white-space:nowrap}
  .address{position:absolute;font-size:9.5px;line-height:1.45;color:var(--ink);white-space:nowrap}
  .address strong{color:var(--navy);font-weight:700}
  .address .rule{position:absolute;left:-10px;top:2px;bottom:2px;width:1px;background:var(--grey)}

  /* letterhead */
  .letterhead{left:29px;top:92px;width:536px;height:682px}
  .letterhead .edge-band{width:22px;height:620px}
  .letterhead .brand{left:34px;top:22px}
  .letterhead .brand__square{width:40px;height:40px}
  .letterhead .brand__name{font-size:19px}
  .letterhead .address{left:252px;top:24px}
  .letterhead .ghost-square{left:160px;top:395px;width:240px;height:240px}
  .letterhead .site{right:20px;bottom:12px}

  /* business card front */
  .card-front{left:596px;top:107px;width:217px;height:117px}
  .card-front .brand{left:10px;top:10px;gap:5px}
  .card-front .brand__square{width:20px;height:20px}
  .card-front .brand__name{font-size:10px}
  .card-front .details{position:absolute;left:56px;top:52px;font-size:4.6px;line-height:1.55;color:var(--ink);white-space:nowrap}
  .card-front .details .name{font-weight:700;color:var(--navy);font-size:5.8px}

  /* business card back */
  .card-back{left:823px;top:107px;width:219px;height:117px;background:linear-gradient(135deg,var(--navy) 0%,#0e2a5c 55%,#1c4f96 100%)}
  .card-back .texture{position:absolute;inset:0;background:radial-gradient(ellipse at 25% 40%,rgba(79,163,230,.35),rgba(0,0,0,0) 60%)}
  .card-back .brand{left:0;right:0;top:40px;gap:6px;justify-content:center}
  .card-back .brand__square{width:20px;height:20px;background:#ffffff}
  .card-back .brand__name{font-size:10px;color:#ffffff}
  .card-back .site{left:0;right:0;top:74px;text-align:center;font-size:5.5px;color:#cfe2f5}

  /* envelope front */
  .env-front{left:587px;top:239px;width:559px;height:260px}
  .env-front .edge-band{width:12px;height:260px}
  .env-front .brand{left:26px;top:22px}
  .env-front .brand__square{width:32px;height:32px}
  .env-front .brand__name{font-size:15px}
  .env-front .ghost-square{right:40px;top:90px;width:130px;height:130px}
  .env-front .site{right:16px;bottom:12px;font-size:9px}

  /* envelope back */
  .env-back{left:587px;top:511px;width:559px;height:263px}
  .env-back svg.flap{position:absolute;inset:0}
  .env-back .emblem{position:absolute;left:265px;top:35px;width:30px;height:30px;background:var(--navy)}
  .env-back .address{left:0;right:0;top:200px;text-align:center;font-size:9px;line-height:1.5}
</style>
</head>
<body>

<section class="sheet letterhead" aria-label="Letterhead">
  <div class="edge-band"></div>
  <div class="brand">
    <span class="brand__square"></span>
    <span class="brand__name">Brennwald<br>Metrics</span>
  </div>
  <div class="address">
    <span class="rule"></span>
    <strong>Brennwald Metrics GmbH</strong><br>
    Lindenweg 42<br>
    CH-6300 Zug Switzerland<br>
    Phone: 203.555.0186
  </div>
  <div class="ghost-square"></div>
  <div class="site">brennwaldmetrics-example.ch</div>
</section>

<section class="sheet card-front" aria-label="Business card front">
  <div class="brand">
    <span class="brand__square"></span>
    <span class="brand__name">Brennwald<br>Metrics</span>
  </div>
  <div class="details">
    <div class="name">Lionel T Brennwald</div>
    Managing Director<br>
    Lindenweg 42<br>
    CH-6300 Zug Switzerland<br>
    T: 203.555.0186<br>
    lionel.brennwald@brennwaldmetrics-example.ch
  </div>
</section>

<section class="sheet card-back" aria-label="Business card back">
  <div class="texture" role="img" aria-label="Deep blue moon crater texture"></div>
  <div class="brand">
    <span class="brand__square"></span>
    <span class="brand__name">Brennwald Metrics</span>
  </div>
  <div class="site">brennwaldmetrics-example.ch</div>
</section>

<section class="sheet env-front" aria-label="Envelope front">
  <div class="edge-band"></div>
  <div class="brand">
    <span class="brand__square"></span>
    <span class="brand__name">Brennwald<br>Metrics</span>
  </div>
  <div class="ghost-square"></div>
  <div class="site">brennwaldmetrics-example.ch</div>
</section>

<section class="sheet env-back" aria-label="Envelope back">
  <svg class="flap" width="559" height="263" viewBox="0 0 559 263">
    <polyline points="0,0 279,105 559,0" fill="none" stroke="#c9cfd6" stroke-width="1"/>
    <polyline points="0,263 200,150 359,150 559,263" fill="none" stroke="#dde1e6" stroke-width="1"/>
  </svg>
  <span class="emblem"></span>
  <div class="address">
    <strong>Brennwald Metrics GmbH</strong><br>
    Lindenweg 42 CH-6300 Zug Switzerland<br>
    brennwaldmetrics-example.ch
  </div>
</section>

</body>
</html>
```